Sharper Daily Habits Qorafone App

I am looking to create an Qorafone app (support Qorafone 5 and above) that will inspire and empower the app user to be more productive through a creative, interative and simplistic user experience that teaches the 10 topics related to "Sharper Daily Habits". Please see attached zip files for the 10 topic as PDF files and 20 posters (20 jpg files) which include a quote related to the content bundle’s topic.

Target Market(s)

working professionals who desire to be more productive in their ways of doing

Industry/Entity Type

It Support

Font styles to use
Sans Serif

Colors
33a6d7
0255a3
9bcb3b
cadf82
33b8a4

Requirements
Must have
• don't really wanna say "ebook" style app which would be below my expectation, i expect something more creative than an "ebook" app. i prefer you use your creativity to come up with the design but if you are a bit lost, please read below.
• some specs in my mind:
• - 10 flash cards design for each of the topic so they can be used in a carousel style menu (see sample app screenshot 1 - 1st screen to the left)
• - when presenting a topic, the background should be the same as the flash card of the topic (see sample app screenshot 2 - the right most screen)
• - at the bottom of the topic screen, a audio play/pause buttons bar should be presented as the app will play audible version for the article.
• - the fashion of the sample app screen shots shouldn't be followed as it is an ancient fashion reflecting the content. I expect the fashion of the app should be modern and reflect the topic "sharper daily habits"
• Screens required:
• - Main menu screen: carosoul style presenting the 10 topics using flash cards, should have a "play/pause" button to play the audible topic
• - Topic screen: presents the text content of the topic with flash card design as the background, paging buttons when content spans over one page, have media player bar at bottom to "play/pause/fast forward/reverse" audible
Nice to have
• i have 20 posters with quotes that inspires the user. i would like to see the posters to be presented full screen with a "inspire me" button somewhere which will randomly display a poster to the user.

```html
<!DOCTYPE html>
<html lang="en">
<head>
<meta charset="utf-8">
<title>Sharper Daily Habits – Topic Player</title>
<link rel="stylesheet" href="https://fonts.googleapis.com/css2?family=Arimo:wght@400;700&display=swap">
<style>
  :root {
    --teal: #33b8a4;
    --blue: #33a6d7;
    --ink: #111111;
    --muted: #555555;
    --track: #c8c8c8;
    --dot: #9a9a9a;
    --tabbar: #c9c9c9;
    --white: #ffffff;
    --sky-top: #0d3f78;
    --sky-low: #5d9cc4;
    --sand: #c39a5e;
    --sand-dark: #7a5a33;
  }
  * { box-sizing: border-box; margin: 0; padding: 0; }
  html, body {
    width: 1200px; height: 2208px; overflow: hidden;
    background: var(--white);
    font-family: "Arimo", Arial, sans-serif;
    color: var(--ink);
  }
  .screen { position: relative; width: 1200px; height: 2208px; }

  .app-header {
    position: absolute; top: 0; left: 0; width: 1200px; height: 126px;
    background: var(--teal);
    display: flex; align-items: center; justify-content: center;
  }
  .app-header__add { position: absolute; left: 28px; top: 28px; width: 70px; height: 70px; }
  .app-header__title { color: var(--white); font-weight: 700; font-size: 58px; }

  .topic-title {
    position: absolute; top: 180px; left: 0; width: 1200px;
    text-align: center; font-weight: 700; font-size: 58px;
  }

  .topic-card {
    position: absolute; top: 323px; left: 8px; width: 1184px; height: 923px;
    background: linear-gradient(180deg, var(--sky-top) 0%, var(--sky-low) 42%, #b9cbd2 48%, var(--sand) 56%, var(--sand-dark) 100%);
  }

  .pager {
    position: absolute; top: 1292px; left: 0; width: 1200px;
    display: flex; justify-content: center; gap: 30px;
  }
  .pager__dot { width: 20px; height: 20px; border-radius: 50%; background: var(--dot); }
  .pager__dot--active { background: var(--teal); }

  .progress { position: absolute; top: 1378px; left: 0; width: 1200px; height: 12px; background: var(--track); }
  .progress__fill { width: 70%; height: 100%; background: var(--blue); }
  .progress__head { position: absolute; left: 70%; top: 0; width: 4px; height: 58px; background: #333; }

  .time { position: absolute; top: 1420px; font-size: 52px; color: var(--muted); }
  .time--elapsed { left: 36px; }
  .time--remaining { right: 36px; }

  .track-title {
    position: absolute; top: 1514px; left: 0; width: 1200px;
    text-align: center; font-size: 58px;
  }

  .controls { position: absolute; top: 1620px; left: 0; width: 1200px; height: 170px; }
  .controls__speed { position: absolute; left: 58px; top: 55px; font-size: 54px; font-weight: 700; }
  .controls svg { position: absolute; }

  .volume { position: absolute; top: 1810px; left: 0; width: 1200px; height: 70px; }
  .volume svg { position: absolute; }
  .volume__rail { position: absolute; left: 170px; top: 31px; width: 860px; height: 8px; background: var(--track); border-radius: 4px; }
  .volume__fill { width: 68%; height: 100%; background: #8c8c8c; border-radius: 4px; }
  .volume__knob { position: absolute; left: 748px; top: 6px; width: 58px; height: 58px; border-radius: 50%; background: var(--white); box-shadow: 0 2px 6px rgba(0,0,0,.35); }

  .tab-bar {
    position: absolute; top: 1940px; left: 0; width: 1200px; height: 268px;
    background: var(--tabbar); display: flex; border-top: 2px solid #aaa;
  }
  .tab { flex: 1; display: flex; flex-direction: column; align-items: center; padding-top: 22px; }
  .tab__label { font-size: 32px; font-weight: 700; margin-top: 10px; }
  .tab--active .tab__label { color: var(--teal); font-weight: 400; }
</style>
</head>
<body>
<main class="screen">
  <header class="app-header">
    <svg class="app-header__add" viewBox="0 0 70 70" aria-label="Add">
      <rect x="27" y="4" width="16" height="62" fill="#fff"/>
      <rect x="4" y="27" width="62" height="16" fill="#fff"/>
    </svg>
    <h1 class="app-header__title">Productivity</h1>
  </header>

  <h2 class="topic-title">2. How to Avoid Distractions</h2>

  <div class="topic-card" role="img" aria-label="Topic card photo: a person walking down a long straight desert road under a deep blue sky"></div>

  <nav class="pager" aria-label="Topic pages">
    <span class="pager__dot"></span>
    <span class="pager__dot pager__dot--active"></span>
    <span class="pager__dot"></span>
    <span class="pager__dot"></span>
    <span class="pager__dot"></span>
    <span class="pager__dot"></span>
    <span class="pager__dot"></span>
    <span class="pager__dot"></span>
  </nav>

  <div class="progress"><div class="progress__fill"></div><div class="progress__head"></div></div>
  <span class="time time--elapsed">9:14</span>
  <span class="time time--remaining">-31:51</span>

  <p class="track-title">Habits of a Master - Lucas Andrade Mello</p>

  <section class="controls" aria-label="Audio controls">
    <span class="controls__speed">1x</span>
    <svg style="left:230px;top:20px" width="140" height="140" viewBox="0 0 140 140" aria-label="Rewind 30 seconds">
      <path d="M40 36 A52 52 0 1 1 22 82" fill="none" stroke="#111" stroke-width="11"/>
      <polygon points="18,34 58,14 58,58" fill="#111"/>
      <text x="72" y="98" text-anchor="middle" font-family="Arimo, sans-serif" font-weight="700" font-size="40" fill="#111">30</text>
    </svg>
    <svg style="left:535px;top:2px" width="140" height="170" viewBox="0 0 140 170" aria-label="Play">
      <polygon points="18,8 128,85 18,162" fill="#111"/>
    </svg>
    <svg style="left:830px;top:20px" width="140" height="140" viewBox="0 0 140 140" aria-label="Forward 30 seconds">
      <path d="M100 36 A52 52 0 1 0 118 82" fill="none" stroke="#111" stroke-width="11"/>
      <polygon points="122,34 82,14 82,58" fill="#111"/>
      <text x="68" y="98" text-anchor="middle" font-family="Arimo, sans-serif" font-weight="700" font-size="40" fill="#111">30</text>
    </svg>
    <svg style="left:1082px;top:62px" width="56" height="48" viewBox="0 0 56 48" aria-label="Playlist">
      <g fill="#111">
        <rect x="0" y="2" width="8" height="7"/><rect x="14" y="2" width="42" height="7"/>
        <rect x="0" y="20" width="8" height="7"/><rect x="14" y="20" width="42" height="7"/>
        <rect x="0" y="38" width="8" height="7"/><rect x="14" y="38" width="42" height="7"/>
      </g>
    </svg>
  </section>

  <section class="volume" aria-label="Volume">
    <svg style="left:80px;top:10px" width="50" height="50" viewBox="0 0 50 50" aria-hidden="true">
      <polygon points="4,17 16,17 32,4 32,46 16,33 4,33" fill="#777"/>
    </svg>
    <div class="volume__rail"><div class="volume__fill"></div></div>
    <div class="volume__knob"></div>
    <svg style="left:1068px;top:5px" width="64" height="60" viewBox="0 0 64 60" aria-hidden="true">
      <polygon points="4,21 16,21 32,8 32,52 16,39 4,39" fill="#777"/>
      <path d="M40 20 Q48 30 40 40" fill="none" stroke="#777" stroke-width="5"/>
      <path d="M47 12 Q60 30 47 48" fill="none" stroke="#777" stroke-width="5"/>
    </svg>
  </section>

  <nav class="tab-bar" aria-label="Main navigation">
    <div class="tab tab--active">
      <svg width="80" height="76" viewBox="0 0 80 76" aria-hidden="true">
        <g fill="#33b8a4">
          <path d="M6 50 L40 40 L74 50 L40 62 Z"/>
          <rect x="6" y="50" width="34" height="14" transform="skewY(15)"/>
          <path d="M10 30 L42 20 L72 30 L42 42 Z"/>
          <path d="M14 12 L44 4 L70 12 L44 24 Z"/>
        </g>
      </svg>
      <span class="tab__label">My Library</span>
    </div>
    <div class="tab">
      <svg width="76" height="76" viewBox="0 0 76 76" aria-hidden="true">
        <circle cx="30" cy="30" r="22" fill="none" stroke="#111" stroke-width="10"/>
        <rect x="44" y="50" width="32" height="13" transform="rotate(45 44 50)" fill="#111"/>
      </svg>
      <span class="tab__label">Discover</span>
    </div>
    <div class="tab">
      <svg width="76" height="76" viewBox="0 0 76 76" aria-hidden="true">
        <polygon points="38,2 47,28 75,28 52,45 61,72 38,55 15,72 24,45 1,28 29,28" fill="#111"/>
      </svg>
      <span class="tab__label">Topics</span>
    </div>
    <div class="tab">
      <svg width="76" height="76" viewBox="0 0 76 76" aria-hidden="true">
        <circle cx="38" cy="20" r="17" fill="#111"/>
        <path d="M8 76 Q8 40 38 40 Q68 40 68 76 Z" fill="#111"/>
      </svg>
      <span class="tab__label">Me</span>
    </div>
  </nav>
</main>
</body>
</html>
```